Business Card Design Project

We are a commercial talent casting company, a very "now" company. We need a new business card that is both current, graphic and elegantly interesting. As we are a service business,
we need something that will attract the attention of new clients,
yet project a business that is 25 years old.

Industry/Entity Type

Business

Requirements
Must have
• 1. Logo - Nora Quillan Casting
2. Address - 47 Thornbury Street
New York, New York 10010
3. Phone - 212-738-4192
4. E-Mail - Casting@noraquillan.example

Nice to have
• Would like the card in black and white with the only accent
color being red.

```html
<!DOCTYPE html>
<html lang="en">
<head>
<meta charset="utf-8">
<title>Nora Quillan Casting — Business Card</title>
<link rel="stylesheet" href="https://fonts.googleapis.com/css2?family=Noto+Sans:wght@400&display=swap">
<style>
  :root {
    --card-black: #080808;
    --accent-red: #ff0000;
    --paper-white: #ffffff;
  }
  html, body {
    margin: 0;
    padding: 0;
    width: 686px;
    height: 1200px;
    overflow: hidden;
    background: var(--card-black);
  }
  .card {
    position: relative;
    width: 686px;
    height: 1200px;
    background: var(--card-black);
    font-family: "Noto Sans", Verdana, sans-serif;
    color: var(--paper-white);
    overflow: hidden;
  }
  .accent-band {
    position: absolute;
    left: 0;
    top: 0;
    width: 63px;
    height: 100%;
    background: var(--accent-red);
  }
  .accent-rule {
    position: absolute;
    left: 64px;
    top: 0;
    width: 3px;
    height: 100%;
    background: var(--paper-white);
  }
  .company-name {
    position: absolute;
    left: 86px;
    top: 156px;
    margin: 0;
    font-weight: 400;
    font-size: 91px;
    line-height: 95px;
    letter-spacing: 0.5px;
  }
  .company-name span { display: block; }
  .contact {
    position: absolute;
    left: 88px;
    margin: 0;
    font-size: 33px;
    line-height: 1;
    white-space: nowrap;
    letter-spacing: 0.3px;
  }
  .contact-street { top: 675px; }
  .contact-city   { top: 736px; }
  .contact-phone  { top: 824px; }
  .contact-email  { top: 910px; }
</style>
</head>
<body>
  <main class="card">
    <div class="accent-band"></div>
    <div class="accent-rule"></div>

    <h1 class="company-name">
      <span>Nora</span>
      <span>Quillan</span>
      <span>Casting</span>
    </h1>

    <p class="contact contact-street">47 Thornbury Street</p>
    <p class="contact contact-city">New York, New York 10010</p>
    <p class="contact contact-phone">212-738-4192</p>
    <p class="contact contact-email">Casting@noraquillan.example</p>
  </main>
</body>
</html>
```